Rack card for marketing

Office to office marketing for knee pain treatment

Target Market(s)

Medical Offices, Retired patients looking to maintain active lifestlye. Family practice medical offices

Industry/Entity Type

Medical

Colors
0054AA
0677BA
7BADD7
CADEEF
E8F1F8

Requirements
Must have
• Font that matches logo, HNS logo, graphic of a retiree who looks active and happy versus a knee graphic
Nice to have
• The best ever rack card!!! Easy to Read, simplicity is key.

```html
<!DOCTYPE html>
<html lang="en">
<head>
<meta charset="utf-8">
<title>HNS Knee Pain Banners</title>
<link href="https://fonts.googleapis.com/css2?family=Montserrat:wght@400;500;600;700;800&display=swap" rel="stylesheet">
<style>
  :root{
    --navy:#0b3561;
    --ink:#0f3f6e;
    --ring:#1d7fb8;
    --steel:#6d7f8f;
    --paper:#f4f5f6;
    --stage:#e6ecee;
    --text:#1f2a33;
    --sky:#7badd7;
    --sky-light:#cadeef;
    --turf:#6f9a5a;
    --skin:#d9a887;
  }
  *{box-sizing:border-box;margin:0;padding:0}
  html,body{width:1200px;height:840px;overflow:hidden;background:var(--stage)}
  body{font-family:'Montserrat',sans-serif;color:var(--text);position:relative}
  .banner{position:absolute;top:30px;width:332px;height:780px;background:var(--paper);overflow:hidden;box-shadow:0 2px 10px rgba(0,0,0,.12)}
  .banner--intro{left:210px}
  .banner--detail{left:658px}
  .wave{position:absolute;left:0;top:0}
  .photo{position:absolute;border-radius:50%;border:6px solid var(--ring)}
  .brand{position:absolute;display:flex;align-items:center;gap:8px}
  .brand__dot{width:14px;height:14px;border-radius:50%;background:var(--ink);flex:none}
  .brand__name{color:var(--ink);font-weight:600}
  .brand__sub{color:var(--steel);font-weight:600}
  .intro-brand{left:28px;top:36px}
  .intro-brand .brand__name{font-size:40px;line-height:1}
  .intro-brand .brand__sub{font-size:15px;margin-top:4px}
  .intro-photo{left:38px;top:116px;width:256px;height:256px;
    background:linear-gradient(180deg,var(--sky-light) 0%,var(--sky) 38%,var(--skin) 52%,#b9876a 64%,var(--turf) 78%,#557d44 100%)}
  .headline{position:absolute;left:0;width:100%;top:482px;text-align:center;color:var(--ink);font-weight:800;font-size:26px;line-height:33px;letter-spacing:.8px}
  .contact{position:absolute;left:0;width:100%;text-align:center}
  .contact__addr{font-size:12px;font-weight:500;line-height:16px;color:#1a1a1a}
  .contact__phone{font-size:27px;font-weight:800;color:var(--ink);letter-spacing:.5px;line-height:32px}
  .contact__fax{font-size:12px;font-weight:500;color:#1a1a1a}
  .intro-contact{top:658px}
  .detail-photo{left:158px;top:24px;width:158px;height:150px;background:radial-gradient(circle at 45% 55%,#a8775e 0 25%,#5b4a3c 55%,#2d3a2a)}
  .detail-title{position:absolute;left:22px;top:42px;color:var(--ink);font-weight:800;font-size:15.5px;line-height:16px}
  .checklist{position:absolute;left:20px;top:118px;list-style:none}
  .checklist li{display:flex;align-items:center;gap:6px;font-size:11px;height:19.6px;color:#253240}
  .checklist li.sub{padding-left:22px;gap:10px}
  .checklist .sq{width:9px;height:9px;background:var(--navy)}
  .section-title{position:absolute;left:0;width:100%;top:356px;text-align:center;color:var(--ink);font-weight:800;font-size:15.5px;letter-spacing:.5px}
  .procedures{position:absolute;left:15px;top:382px;width:302px;display:grid;grid-template-columns:repeat(3,93px);column-gap:10px;row-gap:4px}
  .proc{text-align:center}
  .proc__img{width:93px;height:76px;border:2px solid #4d7da8}
  .proc__label{font-size:10.5px;line-height:11px;margin-top:6px;color:#1a1a1a;min-height:34px}
  .t1{background:linear-gradient(135deg,#d9d9d6,#9ea5a8)}
  .t2{background:linear-gradient(135deg,#9a6a48,#c45a3e 55%,#7c4f35)}
  .t3{background:linear-gradient(135deg,#7a1f26,#e58b8e 55%,#d9b7a8)}
  .t4{background:linear-gradient(135deg,#c9c9c6,#8f979b)}
  .t5{background:linear-gradient(135deg,#c68f6b,#e8b99a 55%,#d6508e)}
  .t6{background:linear-gradient(135deg,#f4f4f4,#b9cbe0)}
  .detail-brand{left:118px;top:630px}
  .detail-brand .brand__dot{width:9px;height:9px}
  .detail-brand .brand__name{font-size:19px;line-height:1}
  .detail-brand .brand__sub{font-size:8px}
  .detail-contact{top:674px}
  .detail-contact .contact__addr{font-size:12.5px}
</style>
</head>
<body>

<section class="banner banner--intro">
  <svg class="wave" width="332" height="780" viewBox="0 0 332 780" aria-hidden="true">
    <path d="M0 178 C110 150 240 112 332 84 L332 292 C240 318 110 360 0 426 Z" fill="var(--navy)"/>
    <path d="M0 426 C110 360 240 318 332 292 L332 310 C240 336 120 372 0 440 Z" fill="#dde2e6"/>
  </svg>
  <div class="brand intro-brand">
    <span class="brand__dot"></span>
    <div>
      <div class="brand__name">HNS</div>
      <div class="brand__sub">Harbor Nerve &amp; Spine</div>
    </div>
  </div>
  <div class="photo intro-photo" role="img" aria-label="Photo of an active, happy retiree walking outdoors on a sunny day"></div>
  <h1 class="headline">COMPREHENSIVE<br>NON-OPERATIVE<br>TREATMENT<br>FOR KNEE PAIN</h1>
  <div class="contact intro-contact">
    <p class="contact__addr">1180 Lakeview Crest Dr.,<br>Oakridge, FL 34000</p>
    <p class="contact__phone">555-014-2290</p>
    <p class="contact__fax">F: 555-014-2291</p>
  </div>
</section>

<section class="banner banner--detail">
  <svg class="wave" width="332" height="780" viewBox="0 0 332 780" aria-hidden="true">
    <path d="M40 0 L332 0 L332 202 C300 120 230 40 40 0 Z" fill="var(--navy)"/>
  </svg>
  <div class="photo detail-photo" role="img" aria-label="Photo of an active person holding their knee outdoors"></div>
  <h2 class="detail-title">Comprehensive<br>Non-operative<br>Treatment<br>for Knee Pain</h2>
  <ul class="checklist">
    <li><svg width="13" height="13" viewBox="0 0 13 13"><rect x="1" y="2" width="10" height="10" fill="none" stroke="var(--navy)" stroke-width="1.5"/><path d="M3 6.5 L6 9.5 L12 1" fill="none" stroke="var(--navy)" stroke-width="2"/></svg>Nonsurgical Options</li>
    <li><svg width="13" height="13" viewBox="0 0 13 13"><rect x="1" y="2" width="10" height="10" fill="none" stroke="var(--navy)" stroke-width="1.5"/><path d="M3 6.5 L6 9.5 L12 1" fill="none" stroke="var(--navy)" stroke-width="2"/></svg>Customized Bracing</li>
    <li><svg width="13" height="13" viewBox="0 0 13 13"><rect x="1" y="2" width="10" height="10" fill="none" stroke="var(--navy)" stroke-width="1.5"/><path d="M3 6.5 L6 9.5 L12 1" fill="none" stroke="var(--navy)" stroke-width="2"/></svg>Topical Medications</li>
    <li><svg width="13" height="13" viewBox="0 0 13 13"><rect x="1" y="2" width="10" height="10" fill="none" stroke="var(--navy)" stroke-width="1.5"/><path d="M3 6.5 L6 9.5 L12 1" fill="none" stroke="var(--navy)" stroke-width="2"/></svg>Topical Supplements</li>
    <li><svg width="13" height="13" viewBox="0 0 13 13"><rect x="1" y="2" width="10" height="10" fill="none" stroke="var(--navy)" stroke-width="1.5"/><path d="M3 6.5 L6 9.5 L12 1" fill="none" stroke="var(--navy)" stroke-width="2"/></svg>Evidence Based Supplementation</li>
    <li><svg width="13" height="13" viewBox="0 0 13 13"><rect x="1" y="2" width="10" height="10" fill="none" stroke="var(--navy)" stroke-width="1.5"/><path d="M3 6.5 L6 9.5 L12 1" fill="none" stroke="var(--navy)" stroke-width="2"/></svg>Cryotherapy / Cold Compression</li>
    <li><svg width="13" height="13" viewBox="0 0 13 13"><rect x="1" y="2" width="10" height="10" fill="none" stroke="var(--navy)" stroke-width="1.5"/><path d="M3 6.5 L6 9.5 L12 1" fill="none" stroke="var(--navy)" stroke-width="2"/></svg>Acupuncture / Electrical Therapy</li>
    <li><svg width="13" height="13" viewBox="0 0 13 13"><rect x="1" y="2" width="10" height="10" fill="none" stroke="var(--navy)" stroke-width="1.5"/><path d="M3 6.5 L6 9.5 L12 1" fill="none" stroke="var(--navy)" stroke-width="2"/></svg>Exercise Protocols</li>
    <li class="sub"><span class="sq"></span>Athletic Trainer</li>
    <li class="sub"><span class="sq"></span>Exercise Physiologist</li>
    <li class="sub"><span class="sq"></span>Home based exercise options</li>
  </ul>
  <h3 class="section-title">PROCEDURES OFFERED</h3>
  <div class="procedures">
    <div class="proc"><div class="proc__img t1" role="img" aria-label="Illustration of a knee joint receiving an injection"></div><p class="proc__label">Interarticular<br>Knee Injection</p></div>
    <div class="proc"><div class="proc__img t2" role="img" aria-label="Illustration of the pes anserine bursa on the knee"></div><p class="proc__label">Pes Anserine<br>Bursa</p></div>
    <div class="proc"><div class="proc__img t3" role="img" aria-label="Photo of hands on a painful knee"></div><p class="proc__label">Genicular<br>Nerve Block</p></div>
    <div class="proc"><div class="proc__img t4" role="img" aria-label="Illustration of knee joint with ablation target points"></div><p class="proc__label">Genicular<br>Radiofrequency<br>Ablation</p></div>
    <div class="proc"><div class="proc__img t5" role="img" aria-label="Photo of a gloved hand giving a knee injection"></div><p class="proc__label">HA<br>(hyaluronic acid)<br>Injections</p></div>
    <div class="proc"><div class="proc__img t6" role="img" aria-label="Photo of an injection medication box"></div><p class="proc__label">Arnimex<br>Injections</p></div>
  </div>
  <div class="brand detail-brand">
    <span class="brand__dot"></span>
    <div>
      <div class="brand__name">HNS</div>
      <div class="brand__sub">Harbor Nerve &amp; Spine</div>
    </div>
  </div>
  <div class="contact detail-contact">
    <p class="contact__addr">1180 Lakeview Crest Dr., Oakridge, FL 34000</p>
    <p class="contact__phone">555-014-2290</p>
    <p class="contact__fax">F: 555-014-2291</p>
  </div>
</section>

</body>
</html>
```